Brennick Capital Business Cards

These are professional business cards that are for my family office.
Put fake emails and phone numbers as of now until I finalize those components. This family office controls my families investments, assets, and future. The cards should be professional.
..
.
.
.
I just uploaded another variation of a logo I would like to see as a business card to I am inbeteen which logo to use

Target Market(s)

business

Industry/Entity Type

business

Contact Information for Business Card

Professional, wealth related, finance related.

Requirements
Must have
• Logo

```html
<!DOCTYPE html>
<html lang="en">
<head>
<meta charset="utf-8">
<title>Brennick Capital Business Cards</title>
<link rel="stylesheet" href="https://fonts.googleapis.com/css2?family=Cinzel:wght@500;600&family=Outfit:wght@400;600&display=swap">
<style>
  :root {
    --backdrop: #363435;
    --navy: #1a1f2b;
    --white: #ffffff;
    --ink: #1a1f2b;
  }
  * { margin: 0; padding: 0; box-sizing: border-box; }
  html, body {
    width: 1200px;
    height: 1200px;
    overflow: hidden;
    background: var(--backdrop);
  }
  .card {
    position: absolute;
    left: 166px;
    width: 853px;
    height: 487px;
    box-shadow: 0 4px 10px rgba(0,0,0,0.35);
  }
  /* Front */
  .card-front {
    top: 64px;
    background: var(--navy);
  }
  .front-frame {
    position: absolute;
    left: 30px;
    top: 30px;
    width: 792px;
    height: 426px;
    border: 1.5px solid var(--white);
    border-radius: 0 37px 0 37px;
  }
  .front-mark {
    position: absolute;
    left: 334px;
    top: 113px;
  }
  .front-name {
    position: absolute;
    left: 0;
    width: 853px;
    top: 342px;
    text-align: center;
    font-family: "Cinzel", serif;
    font-weight: 600;
    font-size: 44px;
    letter-spacing: 1px;
    color: var(--white);
  }
  /* Back */
  .card-back {
    top: 648px;
    background: var(--navy);
  }
  .back-panel {
    position: absolute;
    left: 11px;
    top: 0;
    right: 0;
    bottom: 10px;
    background: var(--white);
  }
  .back-title {
    position: absolute;
    left: 0;
    width: 853px;
    top: 34px;
    text-align: center;
    font-family: "Cinzel", serif;
    font-weight: 600;
    font-size: 56px;
    letter-spacing: 1px;
    color: var(--ink);
  }
  .name-tab {
    position: absolute;
    left: 0;
    top: 226px;
    width: 33px;
    height: 39px;
    background: var(--navy);
  }
  .person-name {
    position: absolute;
    left: 47px;
    top: 214px;
    font-family: "Outfit", sans-serif;
    font-weight: 600;
    font-size: 46px;
    color: var(--ink);
  }
  .contact-list {
    position: absolute;
    left: 40px;
    top: 311px;
    list-style: none;
  }
  .contact-item {
    display: flex;
    align-items: center;
    height: 42px;
    margin-bottom: 5px;
  }
  .contact-icon {
    width: 45px;
    height: 42px;
    background: var(--navy);
    display: flex;
    align-items: center;
    justify-content: center;
    flex: none;
  }
  .contact-text {
    margin-left: 15px;
    font-family: "Outfit", sans-serif;
    font-weight: 400;
    font-size: 26px;
    color: var(--ink);
  }
  .back-mark {
    position: absolute;
    left: 613px;
    top: 248px;
  }
</style>
</head>
<body>
  <section class="card card-front">
    <div class="front-frame"></div>
    <svg class="front-mark" width="186" height="186" viewBox="0 0 186 186" aria-hidden="true">
      <circle cx="93" cy="93" r="91" fill="none" stroke="#ffffff" stroke-width="3"/>
    </svg>
    <div class="front-name">Brennick Capital</div>
  </section>

  <section class="card card-back">
    <div class="back-panel">
      <div class="back-title">Brennick Capital</div>
    </div>
    <div class="name-tab"></div>
    <div class="person-name">Owen Hartley</div>
    <ul class="contact-list">
      <li class="contact-item">
        <span class="contact-icon">
          <svg width="24" height="24" viewBox="0 0 24 24" aria-hidden="true">
            <path d="M6.6 2.5l3 3.4-1.8 2.4c1.3 2.7 3.3 4.7 6 6l2.4-1.8 3.4 3-1.9 3c-7.6-.6-13.5-6.5-14-14z" fill="none" stroke="#ffffff" stroke-width="1.8" stroke-linejoin="round"/>
          </svg>
        </span>
        <span class="contact-text">123-456-7890</span>
      </li>
      <li class="contact-item">
        <span class="contact-icon">
          <svg width="30" height="20" viewBox="0 0 30 20" aria-hidden="true">
            <rect x="1" y="1" width="28" height="18" fill="none" stroke="#ffffff" stroke-width="1.6"/>
            <path d="M1 1l14 11 14-11M1 19l10-9M29 19l-10-9" fill="none" stroke="#ffffff" stroke-width="1.6"/>
          </svg>
        </span>
        <span class="contact-text">yourmail@email.com</span>
      </li>
      <li class="contact-item">
        <span class="contact-icon">
          <svg width="22" height="30" viewBox="0 0 22 30" aria-hidden="true">
            <path d="M11 28C6 21 2 16 2 11a9 9 0 0 1 18 0c0 5-4 10-9 17z" fill="none" stroke="#ffffff" stroke-width="1.4"/>
            <circle cx="11" cy="11" r="3.5" fill="none" stroke="#ffffff" stroke-width="1.4"/>
          </svg>
        </span>
        <span class="contact-text">your location here</span>
      </li>
    </ul>
    <svg class="back-mark" width="182" height="182" viewBox="0 0 182 182" aria-hidden="true">
      <circle cx="91" cy="91" r="89" fill="none" stroke="#1a1f2b" stroke-width="3"/>
    </svg>
  </section>
</body>
</html>
```